Wordpress Design for my Consulting Company

We want a WordPress site created for our new business. We have created a mock-up of the content we want on the site at https://marcobellweather.example.com/website-5

We are not attached to any of the pictures and just put stock stuff from bloq's editor, which we don't have rights to use outside of bloq.

We are NOT looking to just port this site to WordPress, we are looking for some creative ways to display the content in a more professional artistic sense.

I have included several logo files and a text file with the colors and Fonts used in the logo. We are not looking to change the logo or the colors used in the logo.

The Schedule appointment links to a page that embeds a bookslot.example calendar. https://bookslot.example.com/marco-bellweather/trailguide

The final website domain will be venturelanterns.example

Venture lanterns is a consulting company that works directly with the business owners and leaders of small businesses between 50-200 employees. We help companies make sure they have the right technology to meet their strategic goals. We are the anti-"Computer Guy" and we focus on business outcomes NOT cool technology gadgets.

The final design should communicate business growth and success.

Target Market(s)

Business Owners of companies with 50-200 employees

Coding

Coded - Design and coding required

Number of Pages Required

1 page

Font styles to use
Serif
Other font styles liked:
• Trajan Pro Bold, Open Sans

Requirements
Must have
• Should focus on consulting rather than technology.
• Should show the customer as the hero and we are just their guide.
• Must use the logo provided and the colors and fonts in the text file provided. Any other colors and fonts must be complementary.
• The design should scale for all devices computer, iPad, or phone
Should not have
• Should not focus on technology, we are the anti-"Computer Guy" and we focus on business outcomes NOT cool technology gadgets.

```html
<!DOCTYPE html>
<html lang="en">
<head>
<meta charset="utf-8">
<title>Venture Lanterns — Technology Advisors That Get Business</title>
<link rel="stylesheet" href="https://fonts.googleapis.com/css2?family=Roboto:ital,wght@0,300;0,400;0,500;0,700;1,400&display=swap">
<style>
:root{
  --accent:#c87544;
  --accent-dark:#b1612f;
  --slate:#3b4a53;
  --slate-deep:#2f3c44;
  --ink:#333a40;
  --muted:#5d6469;
  --light:#f5f5f5;
  --grey-btn:#9a9a9a;
  --topbar:#8d8f91;
  --white:#ffffff;
}
*{box-sizing:border-box;margin:0;padding:0}
html,body{width:1200px;height:3659px;overflow:hidden}
body{font-family:'Roboto',sans-serif;color:var(--ink);background:var(--white);position:relative}
.abs{position:absolute}

/* top bar */
.topbar{left:0;top:0;width:1200px;height:30px;background:var(--topbar);color:var(--white);font-size:12px;display:flex;justify-content:flex-end;align-items:center;gap:14px;padding-right:130px}
.topbar .phone{font-weight:700}
.dot{width:12px;height:12px;border-radius:50%;background:var(--accent);display:inline-block}

/* header */
.header{left:0;top:30px;width:1200px;height:80px;background:var(--white);box-shadow:0 2px 6px rgba(0,0,0,.08);z-index:2}
.brand{left:190px;top:18px;display:flex;align-items:center;gap:10px}
.brand-mark{width:40px;height:40px;border-radius:50%;background:var(--accent)}
.brand-name{font-size:20px;font-weight:500;color:var(--slate);letter-spacing:1px;line-height:1}
.nav{left:578px;top:30px;display:flex;align-items:center;gap:20px;font-size:13px;color:var(--slate);letter-spacing:.5px}
.nav .cta{background:var(--accent);color:var(--white);padding:10px 18px;font-weight:500;font-size:14px}

/* hero */
.hero{left:0;top:110px;width:1200px;height:517px;background:linear-gradient(115deg,#6e8792 0%,#9fb3bb 35%,#c5d1d6 60%,#7f959f 100%)}
.hero-shade{left:0;top:110px;width:1200px;height:517px;background:linear-gradient(90deg,rgba(40,55,65,.55) 0%,rgba(40,55,65,.15) 55%,rgba(40,55,65,0) 100%)}
.hero-eyebrow{left:188px;top:238px;color:var(--white);font-size:16px;font-weight:700;letter-spacing:1px}
.hero-bar{left:190px;top:268px;width:6px;height:136px;background:var(--accent)}
.hero-title{left:222px;top:266px;color:var(--white);font-size:42px;font-weight:700;line-height:48px}
.hero-sub{left:222px;top:368px;color:var(--white);font-size:16px;font-weight:700;line-height:20px;width:420px}
.btn{display:flex;align-items:center;justify-content:center;font-size:13px}
.btn-accent{background:var(--accent);color:var(--white)}
.btn-light{background:var(--light);color:var(--ink)}
.hero-btn1{left:188px;top:441px;width:142px;height:36px}
.hero-btn2{left:346px;top:441px;width:168px;height:36px}

/* strategy */
.eyebrow{font-size:14px;font-weight:700;letter-spacing:3px;color:var(--accent);text-align:center;width:1200px;left:0}
.strategy-eyebrow{top:696px}
.section-title{left:0;width:1200px;text-align:center;font-size:29px;font-weight:700;color:var(--slate);line-height:38px}
.strategy-title{top:730px}
.step{width:240px;text-align:center}
.step-icon{margin:0 auto;width:80px;height:80px;position:relative}
.step-name{margin-top:30px;font-size:17px;font-weight:500;color:var(--accent)}
.step-text{margin:16px auto 0;font-size:11.5px;line-height:17px;color:var(--muted);width:205px;height:54px}
.step-btn{margin:26px auto 0;width:134px;height:32px;background:var(--grey-btn);color:var(--white);font-size:12px}
.step-btn.on{background:var(--accent)}

/* advise */
.advise{left:0;top:1190px;width:1200px;height:510px;background:var(--accent)}
.advise-photo{left:630px;top:1190px;width:570px;height:510px;background:linear-gradient(135deg,#e6ecf0 0%,#aebcc6 40%,#5d7080 75%,#2e3c47 100%);clip-path:polygon(80px 0,100% 0,100% 100%,0 100%)}
.advise-label{left:151px;top:1284px;color:var(--white);font-size:14px;font-weight:700;letter-spacing:2.5px}
.advise-text{left:151px;top:1324px;width:530px;color:var(--white);font-size:21px;line-height:37px;letter-spacing:.3px}
.advise-btn{left:151px;top:1547px;width:205px;height:44px;background:var(--light);color:var(--ink);font-size:14px;font-weight:500}

/* tired */
.tired-title{top:1800px;font-size:27px}
.divider-v{left:599px;top:1855px;width:1px;height:370px;background:#e2e2e2}
.pain{width:380px;display:flex;gap:18px;font-size:18px;line-height:28px;color:var(--muted)}
.pain .bullet{flex:none;width:15px;height:15px;border-radius:50%;background:var(--accent);margin-top:6px}
.tired-btn{left:488px;top:2252px;width:222px;height:42px;font-size:14px;font-weight:500}

/* testimonial */
.testimonial{left:0;top:2372px;width:1200px;height:610px;background:radial-gradient(ellipse at 50% 40%,#d6936a 0%,#c87544 55%,#a9582b 100%)}
.testimonial-lead{left:230px;top:2440px;width:740px;text-align:center;color:var(--white);font-size:20px;font-weight:700;line-height:36px}
.rule{left:545px;top:2604px;width:110px;height:4px;background:var(--white)}
.quote{left:250px;top:2655px;width:700px;text-align:center;color:var(--white);font-size:18px;font-style:italic;line-height:33px}
.qmark{font-size:42px;font-style:normal;font-weight:700;line-height:0;vertical-align:-12px}
.avatar{left:565px;top:2782px;width:70px;height:70px;border-radius:50%;background:#8a6b58;border:3px solid rgba(255,255,255,.7)}
.person{left:0;top:2864px;width:1200px;text-align:center;color:var(--white)}
.person b{display:block;font-size:16px;font-weight:700}
.person i{font-size:14px}

/* contact */
.contact{left:0;top:2982px;width:1200px;height:677px;background:var(--slate)}
.contact-title{top:3052px;color:var(--white);font-size:40px}
.contact-rule{left:555px;top:3108px;width:90px;height:4px;background:var(--white)}
.field{border:2px solid #e8e8e8;color:var(--white);font-size:15px;padding:8px 10px}
.submit{left:261px;top:3416px;width:139px;height:49px;font-size:18px;font-weight:700}
.info-title{left:764px;top:3185px;color:var(--white);font-size:16px;font-weight:700}
.info{left:764px;display:flex;gap:18px;color:var(--white);font-size:13px;line-height:19px}
.info svg{flex:none;margin-top:2px}
.info strong{font-size:21px;display:block;margin-top:4px}
.socials{left:798px;top:3414px;display:flex;gap:16px}
.socials span{width:12px;height:12px;border-radius:50%;background:var(--white)}
.socials span.alt{background:var(--accent)}
.footer-rule{left:122px;top:3543px;width:956px;height:1px;background:#75838b}
.copyright{left:0;top:3570px;width:1200px;text-align:center;color:var(--white);font-size:14px}
</style>
</head>
<body>

<div class="abs topbar">
  <span>✉ bellweather@venturelanterns.example</span><span>|</span>
  <span>Call <span class="phone">(555) 014-0580</span></span><span>|</span>
  <span class="dot"></span><span class="dot"></span><span class="dot"></span>
</div>

<header class="abs header">
  <div class="abs brand"><span class="brand-mark"></span><span class="brand-name">VENTURE LANTERNS</span></div>
  <nav class="abs nav">
    <svg width="16" height="14" viewBox="0 0 16 14"><path d="M8 0 0 7h2v7h4V9h4v5h4V7h2z" fill="var(--accent)"/></svg>
    <span>ABOUT US</span><span>SERVICES</span>
    <span class="cta">Schedule Appointment</span>
    <svg width="14" height="14" viewBox="0 0 14 14"><circle cx="6" cy="6" r="4.5" fill="none" stroke="var(--slate)" stroke-width="2"/><path d="M9.5 9.5 13 13" stroke="var(--slate)" stroke-width="2"/></svg>
    <svg width="20" height="14" viewBox="0 0 20 14"><path d="M0 2h20M0 7h20M0 12h20" stroke="var(--slate)" stroke-width="2"/></svg>
  </nav>
</header>

<section>
  <div class="abs hero" role="img" aria-label="Photo of three business people in an office meeting"></div>
  <div class="abs hero-shade"></div>
  <div class="abs hero-eyebrow">WELCOME TO VENTURE LANTERNS</div>
  <div class="abs hero-bar"></div>
  <h1 class="abs hero-title">Technology Advisors<br>That "Get" Business</h1>
  <p class="abs hero-sub">We help you leverage technology to create a competitive advantage.</p>
  <a class="abs btn btn-accent hero-btn1">Learn More</a>
  <a class="abs btn btn-light hero-btn2">Schedule Appointment</a>
</section>

<section>
  <div class="abs eyebrow strategy-eyebrow">STRATEGY</div>
  <h2 class="abs section-title strategy-title">The 4 Steps to Aligning Technology<br>to your Business Strategy!</h2>

  <svg class="abs" style="left:0;top:850px" width="1200" height="100" viewBox="0 0 1200 100">
    <g fill="none" stroke="#333" stroke-width="2">
      <path d="M330 48 q30 -22 62 -4"/><path d="M384 38l9 6-10 4"/>
      <path d="M592 52 q36 22 72 -4"/><path d="M654 44l10 4-8 8"/>
      <path d="M825 48 q34 -22 66 -4"/><path d="M882 38l9 6-10 4"/>
    </g>
  </svg>

  <div class="abs step" style="left:124px;top:855px">
    <div class="step-icon">
      <svg width="80" height="80" viewBox="0 0 80 80"><circle cx="38" cy="42" r="34" fill="none" stroke="var(--accent)" stroke-width="2"/><circle cx="38" cy="42" r="24" fill="none" stroke="var(--accent)" stroke-width="1.5"/><circle cx="36" cy="40" r="7" fill="none" stroke="var(--accent)" stroke-width="2.5"/><path d="M41 45l6 6" stroke="var(--accent)" stroke-width="3"/><circle cx="66" cy="14" r="11" fill="var(--accent)"/><text x="66" y="19" text-anchor="middle" font-size="13" font-weight="700" fill="#fff" font-family="Roboto,sans-serif">1</text></svg>
    </div>
    <div class="step-name">Discover</div>
    <p class="step-text">Identify what is going on behind the scenes, and create a snapshot of the current infrastructure.</p>
    <div class="btn step-btn">Learn More</div>
  </div>

  <div class="abs step" style="left:387px;top:855px">
    <div class="step-icon">
      <svg width="80" height="80" viewBox="0 0 80 80"><circle cx="38" cy="42" r="34" fill="var(--accent)" stroke="var(--accent)" stroke-width="2"/><circle cx="38" cy="42" r="26" fill="none" stroke="#fff" stroke-width="1.5"/><rect x="28" y="33" width="20" height="18" fill="none" stroke="#fff" stroke-width="2"/><path d="M28 38h20M33 43h2M38 43h2M43 43h2M33 47h2M38 47h2" stroke="#fff" stroke-width="2"/><circle cx="66" cy="14" r="11" fill="var(--accent)" stroke="#fff" stroke-width="2"/><text x="66" y="19" text-anchor="middle" font-size="13" font-weight="700" fill="#fff" font-family="Roboto,sans-serif">2</text></svg>
    </div>
    <div class="step-name">Prioritize</div>
    <p class="step-text">Meet to decide which solutions and policies will have the greatest impact on reaching the companies goals.</p>
    <div class="btn step-btn">Learn More</div>
  </div>

  <div class="abs step" style="left:649px;top:855px">
    <div class="step-icon">
      <svg width="80" height="80" viewBox="0 0 80 80"><circle cx="38" cy="42" r="34" fill="none" stroke="var(--accent)" stroke-width="2"/><circle cx="38" cy="42" r="24" fill="none" stroke="var(--accent)" stroke-width="1.5"/><path d="M30 50 46 34M40 33h7v7M30 42l-3 3 8 8 3-3" fill="none" stroke="var(--accent)" stroke-width="2.5"/><circle cx="66" cy="14" r="11" fill="var(--accent)"/><text x="66" y="19" text-anchor="middle" font-size="13" font-weight="700" fill="#fff" font-family="Roboto,sans-serif">3</text></svg>
    </div>
    <div class="step-name">Implement</div>
    <p class="step-text">Implement those things that will give the greatest return on investment.</p>
    <div class="btn step-btn on">Learn More</div>
  </div>

  <div class="abs step" style="left:844px;top:855px">
    <div class="step-icon">
      <svg width="80" height="80" viewBox="0 0 80 80"><circle cx="38" cy="42" r="34" fill="none" stroke="var(--accent)" stroke-width="2"/><circle cx="38" cy="42" r="24" fill="none" stroke="var(--accent)" stroke-width="1.5"/><path d="M29 52v-5M35 52v-9M41 52v-13M47 52v-17" stroke="var(--accent)" stroke-width="3"/><circle cx="66" cy="14" r="11" fill="var(--accent)"/><text x="66" y="19" text-anchor="middle" font-size="13" font-weight="700" fill="#fff" font-family="Roboto,sans-serif">4</text></svg>
    </div>
    <div class="step-name">Maintain</div>
    <p class="step-text">Create a system that keeps your technology aligned as strategy adjusts over time.</p>
    <div class="btn step-btn">Learn More</div>
  </div>
</section>

<section>
  <div class="abs advise"></div>
  <div class="abs advise-photo" role="img" aria-label="Photo of hands reviewing business charts and a laptop on a desk"></div>
  <div class="abs advise-label">VENTURE LANTERNS ADVISE</div>
  <p class="abs advise-text">Computer guys frustrate business leaders because they don't have a business mindset. Venture Lanterns advises on strategy that helps companies apply technology to gain a competitive advantage.</p>
  <a class="abs btn advise-btn">Get the best Advise &nbsp;›</a>
</section>

<section>
  <h2 class="abs section-title tired-title">Are you tired of "Computer Guys" that...</h2>
  <div class="abs divider-v"></div>
  <div class="abs pain" style="left:171px;top:1883px"><span class="bullet"></span><span>Don't want to be involved in business strategy.</span></div>
  <div class="abs pain" style="left:171px;top:1978px"><span class="bullet"></span><span>Say "No!" but do not give options on how to achieve your business outcome.</span></div>
  <div class="abs pain" style="left:171px;top:2103px"><span class="bullet"></span><span>Can't explain how a technology will create business value, but insist it is necessary.</span></div>
  <div class="abs pain" style="left:652px;top:1883px"><span class="bullet"></span><span>Give you the excuse, "You never asked."</span></div>
  <div class="abs pain" style="left:652px;top:1978px"><span class="bullet"></span><span>Recommend technology when a simple process or policy change would have the same effect.</span></div>
  <div class="abs pain" style="left:652px;top:2103px"><span class="bullet"></span><span>Suggest expensive solutions that are just thrown away, soon after they are deployed.</span></div>
  <a class="abs btn btn-accent tired-btn">Schedule Appointment &nbsp;›</a>
</section>

<section>
  <div class="abs testimonial" role="img" aria-label="Warm-toned photo of a team celebrating a success"></div>
  <p class="abs testimonial-lead">We get the frustration of working with consultants and experts who don't listen or take the time to understand your company goals and vision. We believe technology should serve your business, not the other way around.</p>
  <div class="abs rule"></div>
  <svg class="abs" style="left:108px;top:2686px" width="20" height="30" viewBox="0 0 20 30"><path d="M16 2 4 15l12 13" fill="none" stroke="#fff" stroke-width="2"/></svg>
  <svg class="abs" style="left:1070px;top:2686px" width="20" height="30" viewBox="0 0 20 30"><path d="M4 2l12 13L4 28" fill="none" stroke="#fff" stroke-width="2"/></svg>
  <p class="abs quote"><span class="qmark">“</span> "Marco and the team at Venture Lanterns are in all our strategy meetings whether or not we think technology will be discussed. And, they have brought great insight to better let us meet our goals. <span class="qmark">”</span></p>
  <div class="abs avatar" role="img" aria-label="Portrait photo of the client"></div>
  <div class="abs person"><b>DALE WHITFORD</b><i>Cedar Hollow Fellowship</i></div>
</section>

<section>
  <div class="abs contact"></div>
  <h2 class="abs section-title contact-title">Contact Us</h2>
  <div class="abs contact-rule"></div>
  <div class="abs field" style="left:261px;top:3179px;width:207px;height:37px">Name</div>
  <div class="abs field" style="left:481px;top:3179px;width:207px;height:37px">Email</div>
  <div class="abs field" style="left:261px;top:3233px;width:207px;height:37px">Phone No.</div>
  <div class="abs field" style="left:481px;top:3233px;width:207px;height:37px">Subject</div>
  <div class="abs field" style="left:261px;top:3289px;width:427px;height:107px">Message</div>
  <a class="abs btn btn-accent submit">Submit ➤</a>

  <div class="abs info-title">Contact Info:</div>
  <div class="abs info" style="top:3222px">
    <svg width="16" height="20" viewBox="0 0 16 20"><path d="M8 1a6 6 0 0 0-6 6c0 5 6 12 6 12s6-7 6-12a6 6 0 0 0-6-6z" fill="none" stroke="#fff" stroke-width="1.5"/><circle cx="8" cy="7" r="2" fill="none" stroke="#fff" stroke-width="1.5"/></svg>
    <span>1420 Harbor Ridge Parkway,<br>Suite 200 Lakeview Station,<br>TX 77001</span>
  </div>
  <div class="abs info" style="top:3303px">
    <svg width="18" height="18" viewBox="0 0 18 18"><path d="M4 1l3 4-2 2c1 3 3 5 6 6l2-2 4 3-2 3C8 17 1 10 1 3z" fill="none" stroke="#fff" stroke-width="1.5"/></svg>
    <span>CALL TODAY!<strong>(555) 014-0580</strong></span>
  </div>
  <div class="abs info" style="top:3372px">
    <svg width="18" height="14" viewBox="0 0 18 14"><rect x="1" y="1" width="16" height="12" fill="none" stroke="#fff" stroke-width="1.5"/><path d="M1 1l8 7 8-7" fill="none" stroke="#fff" stroke-width="1.5"/></svg>
    <span>bellweather@venturelanterns.example</span>
  </div>
  <div class="abs socials"><span></span><span class="alt"></span><span></span></div>

  <div class="abs footer-rule"></div>
  <div class="abs copyright">© Copyright ©2018 by Venture Lanterns</div>
</section>

</body>
</html>
```